Business Card Design Project

I am a new business offering a consulting service in Homeware buying, product development and trend forecasting. I would like to use colours that are current and on trend now. Needs to be eye catching, speak of creativity and design.

Front: Matt charcoal card with black gloss embossing name print
Back: white with Pink text

Pink pantone: 812c

Target Market(s)

Retailers and Wholesalers of Homeware products

Industry/Entity Type

Business

Requirements
Must have
• Please go to this link and the card on this link is what I am looking for.

http://www.foliorama.net/gallery/Blank_sheet-KX/402817

1. Card Front

Name on front of card: MARGOT FINCHLEY

2. Back card

The following text must be designed onto the card:

Address: 17 Walloway Street ,Paddington, 2021, NSW, Sydney, Australia
Mobile: +61 (0)412305718
Email: finchmel@wirrolink.net.au

Homeware trends
Product development and sourcing
Strategic Buying management
Nice to have
• Creativity in selection of font, composition and proportion.
Should not have
• I don't want to see graphics/shapes on the card.

```html
<!DOCTYPE html>
<html lang="en">
<head>
<meta charset="utf-8">
<title>Margot Finchley – Business Card</title>
<link href="https://fonts.googleapis.com/css2?family=Audiowide&family=Arimo:wght@700&display=swap" rel="stylesheet">
<style>
  :root {
    --backdrop: #3b3b3d;
    --charcoal: #202226;
    --emboss-ink: #1a1c1f;
    --emboss-light: rgba(255,255,255,0.07);
    --emboss-dark: rgba(0,0,0,0.55);
    --pink: #ef5a9e;
    --ink: #0b0b0c;
  }
  html, body {
    margin: 0;
    width: 1200px;
    height: 534px;
    overflow: hidden;
    background: var(--backdrop);
  }
  .stage {
    position: relative;
    width: 1200px;
    height: 534px;
  }
  .card {
    position: absolute;
    top: 119px;
    width: 517px;
    height: 295px;
    box-sizing: border-box;
  }
  .card--front {
    left: 62px;
    background: var(--charcoal);
    display: flex;
    align-items: center;
    justify-content: center;
  }
  .card--back {
    left: 619px;
    background: var(--pink);
    padding: 58px 0 0 42px;
    color: var(--ink);
    font-family: "Arimo", Arial, sans-serif;
    font-weight: 700;
  }
  .front-name {
    font-family: "Audiowide", sans-serif;
    font-size: 34px;
    color: var(--emboss-ink);
    letter-spacing: 0.5px;
    text-shadow: -1px -1px 0 var(--emboss-light), 1px 1px 1px var(--emboss-dark);
    margin: 16px 0 0;
    white-space: nowrap;
  }
  .back-name {
    font-family: "Audiowide", sans-serif;
    font-weight: 400;
    font-size: 32px;
    margin: 0 0 12px;
    line-height: 1;
    white-space: nowrap;
  }
  .services {
    list-style: none;
    margin: 0 0 14px;
    padding: 0 0 0 4px;
    font-size: 12.5px;
    line-height: 16px;
  }
  .services li::before {
    content: "•";
    margin-right: 6px;
  }
  .address {
    margin: 0 0 8px;
    font-size: 12.5px;
    line-height: 16px;
  }
  .contact {
    margin: 0;
    font-size: 12.5px;
    line-height: 16px;
  }
</style>
</head>
<body>
<main class="stage">
  <section class="card card--front" aria-label="Card front">
    <h1 class="front-name">Margot Finchley</h1>
  </section>
  <section class="card card--back" aria-label="Card back">
    <h2 class="back-name">Margot Finchley</h2>
    <ul class="services">
      <li>Homeware trends</li>
      <li>Product developement and sourcing</li>
      <li>Strategic Buying management</li>
    </ul>
    <p class="address">17 Walloway Street ,Paddington, 2021, NSW, Sydney, Australia</p>
    <p class="contact">m: +61 (0)412305718<br>e: finchmel@wirrolink.net.au</p>
  </section>
</main>
</body>
</html>
```